Agricultural and Earthmoving business card design

We need a business card design for a new company based in Kilmore, Victoria. We are a versatile company with two specialties, the first is an earthworks side, we do big and small jobs, from soccer fields for councils and football clubs down to house cuts for the public, horse ridding arena's, tennis courts and drainage are also small jobs we have experience in. Not only do we do earthmoving, but we also have a lot of experience in the agricultural side of machinery work, from pasture improvements to a lot of experience in hay contracting. We need a business card that doesn't focus on only one side of our business but blends both skills. We would like a primarily black business card that incorporates our company logo. Our company colours are black red , grey and white.

Industry/Entity Type

House

Contact Information for Business Card

Marwick Contracting, Dale Marwick, 2741 Ferngate Rd Kilmore Vic 3764, Phone: 03 5926 4083, Mobile: 0437 902 618. Specialising in Earthmoving, synthetic and natural turf, landscaping, drainage. Also specialising in Agricultural improvements and hay contracting.

Requirements
Must have
• A good blend of both earthmoving and agricultural contracting. Company logo.

```html
<!DOCTYPE html>
<html lang="en">
<head>
<meta charset="utf-8">
<title>Marwick Contracting — Business Card</title>
<link href="https://fonts.googleapis.com/css2?family=Questrial&display=swap" rel="stylesheet">
<style>
  :root {
    --backdrop: #3b3b3d;
    --card: #1b1d30;
    --accent-blue: #4a78c8;
    --text-light: #e6e8ee;
    --text-muted: #c9ccd6;
    --divider: #6b6f82;
  }
  html, body {
    margin: 0;
    padding: 0;
    width: 1200px;
    height: 807px;
    overflow: hidden;
    background: var(--backdrop);
  }
  .canvas {
    position: relative;
    width: 1200px;
    height: 807px;
    display: flex;
    align-items: center;
    justify-content: center;
    gap: 44px;
  }
  .card {
    position: relative;
    width: 520px;
    height: 300px;
    background: var(--card);
    box-shadow: 0 10px 28px rgba(0, 0, 0, 0.45);
    font-family: "Questrial", "Century Gothic", sans-serif;
    box-sizing: border-box;
    padding: 0 28px;
  }
  .card-front {
    display: flex;
    flex-direction: column;
    align-items: center;
    justify-content: center;
  }
  .brand-name {
    color: var(--accent-blue);
    font-size: 34px;
    letter-spacing: 0.5px;
    margin: 0 0 34px;
    font-weight: 400;
    white-space: nowrap;
  }
  .services {
    text-align: center;
    color: var(--text-muted);
    font-size: 9px;
    letter-spacing: 0.4px;
    line-height: 2;
    text-transform: uppercase;
    white-space: nowrap;
  }
  .services .sep {
    display: inline-block;
    width: 1px;
    height: 10px;
    background: var(--divider);
    margin: 0 6px;
    vertical-align: -1px;
  }
  .card-back {
    display: flex;
    flex-direction: column;
    align-items: center;
    justify-content: center;
    text-align: center;
  }
  .person-name {
    color: var(--accent-blue);
    font-size: 30px;
    margin: 0 0 12px;
    font-weight: 400;
    letter-spacing: 0.5px;
  }
  .contact {
    color: var(--text-light);
    font-size: 16px;
    line-height: 1.4;
    font-style: normal;
    white-space: nowrap;
  }
</style>
</head>
<body>
  <main class="canvas">
    <section class="card card-front" aria-label="Card front">
      <h1 class="brand-name">Marwick Contracting</h1>
      <div class="services">
        <div>Specialising in earthmoving<span class="sep"></span>Synthetic and natural turf<span class="sep"></span>Landscaping&nbsp; drainage</div>
        <div>Specialising in agricultural improvements and hay contracting.</div>
      </div>
    </section>
    <section class="card card-back" aria-label="Card back">
      <h2 class="person-name">Dale Marwick</h2>
      <address class="contact">
        P: 03 5926 4083<br>
        M: 0437 902 618<br>
        2741 Ferngate Rd Tallowmere 3999,
      </address>
    </section>
  </main>
</body>
</html>
```